Business Cards Brimsworth Nuptials

I have a new webpage address and would like to update my business cards with Facebook and Instagram links as well. I need assistance with designing it. I have attached an old business card.

Target Market(s)

Potential couples wanting to get married and vendors who work with weddings

Industry/Entity Type

Wedding

Contact Information for Business Card

Name of Company (Brimsworth Nuptials), Pam Holcroft, Phone number (480-762-3038), Webpage: www.brimsworthnuptials4u.example, Facebook Link: Brimsworth Nuptials, Instagram Link: BrimsworthNuptials4u

Colors
0094D4
00A9DD
6FCCEA
C7EBF8
E9F6FB
00AB8E
00BBA5
67D7C9
C6EFE9
E9F9F6

Requirements
Nice to have
• Florals with teal on back of card. Not sure what needs to be on front and what on back
Should not have
• Definitive man/woman couple

```html
<!DOCTYPE html>
<html lang="en">
<head>
<meta charset="utf-8">
<title>Brimsworth Nuptials – Business Cards</title>
<link rel="stylesheet" href="https://fonts.googleapis.com/css2?family=Poppins:wght@400;700&display=swap">
<style>
  :root {
    --backdrop: #e3e3e3;
    --blush: #dfbec8;
    --blush-ink: #dcbcc6;
    --teal-deep: #0a5c5a;
    --teal-bloom: #149a7e;
    --rose-bloom: #e4a7ac;
    --ink: #1c1a1b;
    --icon-teal: #0b5e5b;
    --white: #ffffff;
  }
  * { box-sizing: border-box; margin: 0; padding: 0; }
  html, body { width: 1200px; height: 1101px; overflow: hidden; }
  body {
    background: var(--backdrop);
    font-family: "Poppins", sans-serif;
    position: relative;
  }
  .card {
    position: absolute;
    width: 302px;
    height: 534px;
    overflow: hidden;
  }
  .card--front { left: 246px; top: 266px; background: var(--blush); color: var(--ink); }
  .card--back  { left: 641px; top: 265px; background: var(--teal-deep); }

  .floral { position: absolute; border-radius: 0 0 60% 0; }
  .floral--front-top { left: 0; top: 20px; width: 196px; height: 174px;
    background: radial-gradient(ellipse at 55% 55%, rgba(228,167,172,.55), rgba(228,167,172,0) 70%); }
  .floral--front-bottom { left: 194px; top: 333px; width: 108px; height: 116px; border-radius: 60% 0 0 0;
    background: radial-gradient(ellipse at 50% 45%, rgba(228,167,172,.55), rgba(228,167,172,0) 70%); }
  .floral--back-top { left: 0; top: 0; width: 212px; height: 184px;
    background: radial-gradient(ellipse at 50% 55%, rgba(20,154,126,.6), rgba(20,154,126,0) 70%); }
  .floral--back-bottom { left: 92px; top: 348px; width: 210px; height: 186px; border-radius: 60% 0 0 0;
    background: radial-gradient(ellipse at 55% 45%, rgba(20,154,126,.6), rgba(20,154,126,0) 70%); }

  .holder-name {
    position: absolute; left: 34px; top: 226px;
    font-weight: 700; font-size: 39px; line-height: 46px; letter-spacing: -0.3px;
  }
  .divider { position: absolute; left: 38px; top: 369px; width: 20px; height: 2px; background: var(--ink); }

  .contact-list { position: absolute; left: 36px; top: 424px; list-style: none; }
  .contact-list li {
    display: flex; align-items: center; height: 19px; margin-bottom: 7px;
    font-size: 14px; letter-spacing: 0.6px;
  }
  .contact-icon {
    width: 19px; height: 19px; border-radius: 50%; background: var(--icon-teal);
    margin-right: 7px; flex: none; display: flex; align-items: center; justify-content: center;
  }

  .web {
    position: absolute; left: 260px; top: 32px; width: 20px;
    display: flex; flex-direction: column; align-items: center;
  }
  .web-address {
    writing-mode: vertical-rl; transform: rotate(180deg);
    font-size: 13px; letter-spacing: 0.6px; margin-top: 8px; white-space: nowrap;
  }

  .brand-name {
    position: absolute; left: 0; right: 0; top: 220px; text-align: center;
    color: var(--blush-ink); font-weight: 700; font-size: 34px; line-height: 44px;
  }
</style>
</head>
<body>
  <section class="card card--front" aria-label="Business card front">
    <div class="floral floral--front-top" role="img" aria-label="Hand-drawn pink tulip branch with grey leaves"></div>
    <div class="floral floral--front-bottom" role="img" aria-label="Small hand-drawn pink tulip sprig"></div>

    <div class="web">
      <span class="contact-icon">
        <svg width="13" height="13" viewBox="0 0 14 14" fill="none" stroke="#fff" stroke-width="1.1">
          <circle cx="7" cy="7" r="5.5"/><ellipse cx="7" cy="7" rx="2.4" ry="5.5"/>
          <line x1="1.5" y1="7" x2="12.5" y2="7"/><line x1="2.4" y1="4.3" x2="11.6" y2="4.3"/><line x1="2.4" y1="9.7" x2="11.6" y2="9.7"/>
        </svg>
      </span>
      <span class="web-address">www.brimsworthnuptials4u.example</span>
    </div>

    <h1 class="holder-name">Pam<br>Holcroft</h1>
    <div class="divider"></div>

    <ul class="contact-list">
      <li><span class="contact-icon">
        <svg width="11" height="11" viewBox="0 0 24 24" fill="#fff"><path d="M6.6 10.8a15 15 0 006.6 6.6l2.2-2.2a1 1 0 011-.25 11.4 11.4 0 003.6.57 1 1 0 011 1V20a1 1 0 01-1 1A17 17 0 013 4a1 1 0 011-1h3.5a1 1 0 011 1c0 1.25.2 2.45.57 3.57a1 1 0 01-.25 1z"/></svg>
      </span>480-762-3038</li>
      <li><span class="contact-icon"></span>BrimsworthNuptials4u</li>
      <li><span class="contact-icon"></span>Brimsworth Nuptials</li>
    </ul>
  </section>

  <section class="card card--back" aria-label="Business card back">
    <div class="floral floral--back-top" role="img" aria-label="Hand-drawn teal tulip branch with grey leaves"></div>
    <div class="floral floral--back-bottom" role="img" aria-label="Hand-drawn teal tulip branch with grey leaves"></div>
    <h2 class="brand-name">Brimsworth<br>Nuptials</h2>
  </section>
</body>
</html>
```